Luxury Jewellery Brand Business Card design
A website will be needed shortly after so show your skills
Luxury Jewellery Brand Business Card design  - Jewelry
Creative Brief
Simple
Marcus Delvecky
Creative Director
47D Westbury mansions Westbury place london sw3k 2rt
marcus@lorvanemora.com
www.lorvanemora.com
The phone number provided is for design purpose only the real phone number will replace the temp at the end of the competition
tobiasgrell tobiasgrell
Hello all designers!! I have been very impressed with all the entries so far. I would like to see your best versions with colour . The colors I like are royal puple,racing green ,Red and an all white version . I like grey too but must be a dark grey ... have a go ... Thanks
#10 try it all with the filled in logo
#3 like the size of the logo
Thanks.Your the first to upload Could you possibly try the card using Logo lorvanemora_logo2_47729.jpg that I have uploaded ?
hi guys , Good luck with this one !!!! I am looking for interesting business cards !! simple but memorable!!! Excited to see what you guys come up with.....

```html
<!DOCTYPE html>
<html lang="en">
<head>
<meta charset="utf-8">
<title>Lorvane Mora — Business Card</title>
<link href="https://fonts.googleapis.com/css2?family=Cormorant+Garamond:wght@500&family=Open+Sans:ital,wght@0,400;0,600;1,600&display=swap" rel="stylesheet">
<style>
  :root {
    --stage: #e9e7e4;
    --ink: #111111;
    --card-black: #0d0d0d;
    --pattern-dark: #1c1c1c;
    --pattern-mid: #2e2e2e;
    --paper: #ffffff;
    --rule: #9a9a9a;
    --text: #2a2a2a;
    --muted: #555555;
  }
  * { margin: 0; padding: 0; box-sizing: border-box; }
  html, body { width: 1200px; height: 904px; overflow: hidden; }
  body { background: var(--stage); position: relative; font-family: "Open Sans", sans-serif; color: var(--text); }

  .card { position: absolute; width: 620px; height: 354px; box-shadow: 0 6px 18px rgba(0,0,0,.25); overflow: hidden; }

  /* Back side */
  .card-back { left: 50px; top: 70px; background: var(--card-black); }
  .back-pattern { position: absolute; inset: 0; background: radial-gradient(circle at 40% 45%, var(--pattern-mid), var(--pattern-dark) 70%, var(--card-black)); }
  .back-mark { position: absolute; right: 90px; top: 110px; display: flex; align-items: center; gap: 8px; color: var(--paper); font-family: "Cormorant Garamond", serif; font-weight: 500; font-size: 15px; letter-spacing: 2px; }
  .back-mark .square { width: 22px; height: 22px; background: var(--paper); }

  /* Front side */
  .card-front { left: 530px; top: 480px; background: var(--paper); }
  .brand { position: absolute; left: 34px; top: 48px; display: flex; flex-direction: column; align-items: flex-start; gap: 10px; }
  .brand .square { width: 34px; height: 34px; background: var(--ink); margin-left: 20px; }
  .brand-name { font-family: "Cormorant Garamond", serif; font-weight: 500; font-size: 28px; letter-spacing: 1.5px; color: var(--ink); }
  .person { position: absolute; right: 40px; top: 80px; text-align: right; }
  .person-name { font-weight: 600; font-style: italic; font-size: 14px; color: var(--ink); }
  .person-role { font-size: 11px; color: var(--muted); }
  .divider { position: absolute; left: 34px; right: 34px; top: 128px; height: 1px; background: var(--rule); }

  .contact { position: absolute; left: 34px; top: 152px; font-size: 11px; line-height: 15px; color: var(--text); }
  .contact .address { margin-bottom: 6px; max-width: 220px; }
  .contact-line { display: flex; align-items: center; gap: 6px; }
  .contact-line svg { width: 11px; height: 11px; fill: var(--ink); flex: none; }

  .web-band { position: absolute; right: 0; bottom: 24px; width: 250px; height: 40px; background: var(--ink); display: flex; align-items: center; gap: 12px; padding-left: 14px; }
  .web-band .square { width: 20px; height: 20px; border: 2px solid var(--paper); }
  .web-band .web { color: var(--paper); font-size: 12px; letter-spacing: 1px; }
  .base-band { position: absolute; left: 0; right: 0; bottom: 0; height: 24px; background: var(--ink); }
</style>
</head>
<body>
  <section class="card card-back" aria-label="Card back">
    <div class="back-pattern" role="img" aria-label="Repeating dark monogram pattern"></div>
    <div class="back-mark"><span class="square"></span><span>LORVANE MORA</span></div>
  </section>

  <section class="card card-front" aria-label="Card front">
    <div class="brand">
      <span class="square"></span>
      <span class="brand-name">LORVANE MORA</span>
    </div>
    <div class="person">
      <p class="person-name">Marcus Delvecky</p>
      <p class="person-role">Creative Director</p>
    </div>
    <div class="divider"></div>

    <div class="contact">
      <p class="address">47D Westbury Mansions Westbury<br>Place London SW3K 2RT</p>
      <p class="contact-line">
        <svg viewBox="0 0 12 12"><path d="M1 2.5C1 1.7 1.7 1 2.5 1h7C10.3 1 11 1.7 11 2.5V4H8.5V3h-5v1H1zM2 5h8l1 6H1z"/></svg>
        0044 208 431 5927
      </p>
      <p class="contact-line">
        <svg viewBox="0 0 12 12"><path d="M3.5 0.5h5a1 1 0 0 1 1 1v9a1 1 0 0 1-1 1h-5a1 1 0 0 1-1-1v-9a1 1 0 0 1 1-1zM4 2v7h4V2z"/></svg>
        0044 7812 459 306
      </p>
      <p class="contact-line">
        <svg viewBox="0 0 12 12"><path d="M1 2.5h10v7H1zM1.8 3.3L6 6.5l4.2-3.2v-.1H1.8z"/></svg>
        marcus@lorvanemora.com
      </p>
    </div>

    <div class="web-band">
      <span class="square"></span>
      <span class="web">www.lorvanemora.com</span>
    </div>
    <div class="base-band"></div>
  </section>
</body>
</html>
```